Save the Date postcard for Bellwood School 18th Annual Starfall Soiree - Lunavista: Where the Party

We need a Save the Date postcard for our school's Starfall Soiree fundraiser. Front of postcard should be tropical to invoke the feel of Lunavista, with bright colors, flowers, palm leaves, and fruit. We would like the design to include a logo that could be used for future projects like letterhead and invitation with the selected designer. I will attach a file with a design similar to what I would like to see as well as files from past years for our event.

Info that must be included:
Bellwood 18th Annual Starfall Soiree
Lunavista
Where the Party Never Stops!
March 10, 2018 5:30-Midnight
Brackley Court Hotel - Pellridge Events Center
The back side should leave the right side blank with mailing address space. On the left side, one small graphic like flower or palm leaf on front with the following info:
(Return address) Bellwood Catholic School
482 North Quillan
Calder Falls, TX 75418
(Tagline) Bring your yellow feathers and dancing shoes because music and passion are ALWAYS in fashion...
Save the date for a seat at the hottest spot north of Havana on March 10!
(Footer) Sponsor & Ticket Information soon!
bellwood-acad.org/bwa-starfall-soiree/
Bellwood is a 501(c)(3) organization

Target Market(s)

Affluent supporters and donors, age 21+

Industry/Entity Type

School

Font styles to use
Serif
Decorative

Colors

Designer to choose colors to be used in the design.

Requirements
Must have
• Text as specified in description
Nice to have
• Bright colors, palm leaves, and fruit
Should not have
• Don't use typical lady with fruit on head or anything risque

```html
<!DOCTYPE html>
<html lang="en">
<head>
<meta charset="utf-8">
<title>Bellwood Starfall Soiree – Save the Date Postcard</title>
<link rel="stylesheet" href="https://fonts.googleapis.com/css2?family=Dancing+Script:wght@600;700&family=Mali:wght@500&family=Lilita+One&family=Playfair+Display:wght@500&family=Oswald:wght@600&family=Roboto+Condensed:wght@400&display=block">
<style>
  :root {
    --backdrop: #ece9e4;
    --card-orange: #ee6b2f;
    --gold-light: #f6d77a;
    --gold-mid: #d9a93a;
    --gold-dark: #a87516;
    --white: #ffffff;
    --ink: #2b2420;
    --ocean: #1c8bc9;
    --ocean-deep: #1479b3;
    --peach: #f4b49b;
    --stamp-grey: #a7a7a7;
    --navy: #1f3b8f;
  }
  * { box-sizing: border-box; margin: 0; padding: 0; }
  html, body { width: 1200px; height: 528px; overflow: hidden; }
  body { background: var(--backdrop); position: relative; }

  .postcard {
    position: absolute;
    top: 52px;
    width: 542px;
    height: 428px;
    box-shadow: 0 3px 10px rgba(0,0,0,.25);
    overflow: hidden;
  }

  /* ---------- Front ---------- */
  .postcard--front { left: 40px; background: var(--card-orange); }
  .foil-frame {
    position: absolute;
    inset: 14px;
    border: 12px solid var(--gold-mid);
    border-image: linear-gradient(135deg, var(--gold-light), var(--gold-dark) 25%, var(--gold-light) 50%, var(--gold-mid) 75%, var(--gold-light)) 1;
  }
  .event-title {
    position: absolute;
    top: 30px; left: 0; right: 0;
    text-align: center;
    font-family: "Dancing Script", cursive;
    font-weight: 600;
    font-size: 27px;
    color: var(--white);
  }
  .event-title sup { font-size: 15px; }
  .tropical-bouquet {
    position: absolute;
    left: 150px; top: 70px;
    width: 260px; height: 250px;
    border-radius: 46% 54% 50% 50%;
    background: radial-gradient(circle at 50% 55%, #e8569a 0%, #d9477f 22%, #4e9a55 48%, #2f7a4c 68%, rgba(238,107,47,0) 72%);
  }
  .event-name {
    position: absolute;
    top: 150px; left: 0; right: 0;
    text-align: center;
    font-family: "Lilita One", sans-serif;
    font-size: 64px;
    letter-spacing: 2px;
    color: var(--white);
    text-shadow: 2px 2px 0 #e7c27a, 4px 4px 0 #c98a2c, 6px 8px 8px rgba(0,0,0,.35);
    transform: rotate(-3deg);
  }
  .event-slogan {
    position: absolute;
    top: 248px; left: 0; right: 0;
    text-align: center;
    font-family: "Dancing Script", cursive;
    font-weight: 700;
    font-size: 34px;
    line-height: 34px;
    color: var(--ocean);
    -webkit-text-stroke: 3px var(--white);
    paint-order: stroke fill;
  }
  .event-date {
    position: absolute;
    top: 330px; left: 0; right: 0;
    text-align: center;
    font-family: "Playfair Display", serif;
    font-size: 19px;
    color: var(--white);
  }
  .event-venue {
    position: absolute;
    top: 358px; left: 0; right: 0;
    text-align: center;
    font-family: "Playfair Display", serif;
    font-size: 12px;
    line-height: 15px;
    color: var(--ink);
  }

  /* ---------- Back ---------- */
  .postcard--back {
    left: 617px;
    background: linear-gradient(90deg, var(--peach) 0%, #f8d4c4 28%, var(--white) 50%);
  }
  .tagline {
    position: absolute;
    top: 32px; left: 12px; width: 230px;
    text-align: center;
    font-family: "Mali", cursive;
    font-weight: 500;
    font-size: 13px;
    line-height: 21px;
    color: var(--ink);
    white-space: nowrap;
  }
  .tagline em { font-style: normal; color: var(--ocean); font-size: 14px; }
  .flower-wreath {
    position: absolute;
    left: 28px; top: 126px;
    width: 200px; height: 200px;
    border-radius: 50%;
    background: radial-gradient(circle, #f6a3b4 0%, #e9647f 45%, #45a79b 68%, rgba(244,180,155,0) 72%);
  }
  .save-date-badge {
    position: absolute;
    left: 62px; top: 160px;
    width: 132px; height: 132px;
    border-radius: 50%;
    background: var(--ocean);
    border: 3px solid var(--white);
    color: var(--white);
    font-family: "Roboto Condensed", sans-serif;
    text-align: center;
    padding-top: 26px;
  }
  .save-date-badge .badge-head { font-family: "Oswald", sans-serif; font-size: 17px; line-height: 20px; }
  .save-date-badge .badge-body { font-size: 12px; line-height: 14px; margin-top: 2px; }
  .save-date-badge .badge-date { font-family: "Oswald", sans-serif; font-size: 15px; line-height: 20px; margin-top: 2px; }
  .sponsor-note {
    position: absolute;
    top: 324px; left: 20px; width: 220px;
    text-align: center;
    font-family: "Oswald", sans-serif;
    font-size: 13px;
    color: var(--ink);
  }
  .event-url {
    position: absolute;
    top: 349px; left: 22px; width: 222px;
    background: var(--ocean-deep);
    color: var(--white);
    font-family: "Roboto Condensed", sans-serif;
    font-size: 12px;
    text-align: center;
    padding: 3px 0;
  }
  .nonprofit-note {
    position: absolute;
    top: 374px; left: 20px; width: 226px;
    text-align: center;
    font-family: "Roboto Condensed", sans-serif;
    font-size: 10px;
    color: var(--ink);
  }
  .school-mark {
    position: absolute;
    top: 22px; left: 312px;
    display: flex; align-items: center; gap: 6px;
    font-family: "Roboto Condensed", sans-serif;
    font-size: 10px;
    color: var(--navy);
  }
  .school-mark .mark-square { width: 14px; height: 14px; background: var(--navy); }
  .return-address {
    position: absolute;
    top: 94px; left: 312px;
    font-family: "Roboto Condensed", sans-serif;
    font-style: normal;
    font-size: 11px;
    line-height: 14px;
    color: var(--ink);
  }
  .stamp-box {
    position: absolute;
    top: 20px; right: 20px;
    width: 50px; height: 58px;
    border: 3px solid var(--stamp-grey);
  }
</style>
</head>
<body>

<section class="postcard postcard--front">
  <div class="foil-frame"></div>
  <h1 class="event-title">Bellwood's 18<sup>th</sup> Annual Starfall Soiree</h1>
  <div class="tropical-bouquet" role="img" aria-label="Watercolour tropical bouquet with toucan, pineapple, hibiscus flowers and palm leaves"></div>
  <h2 class="event-name">LUNAVISTA</h2>
  <p class="event-slogan">Where the Party<br>Never Stops!</p>
  <p class="event-date">March 10, 2018 5:30-Midnight</p>
  <p class="event-venue">Brackley Court Hotel<br>Pellridge Events Center</p>
</section>

<section class="postcard postcard--back">
  <p class="tagline">Bring your yellow feathers<br>and dancing shoes because<br>music and passion<br>are <em>Always</em> in fashion...</p>
  <div class="flower-wreath" role="img" aria-label="Watercolour wreath of tropical flowers and leaves"></div>
  <div class="save-date-badge">
    <div class="badge-head">SAVE THE DATE</div>
    <div class="badge-body">for a seat at the hottest<br>spot north of Havana</div>
    <div class="badge-date">on March 10!</div>
  </div>
  <p class="sponsor-note">SPONSOR &amp; TICKET INFORMATION SOON!</p>
  <p class="event-url">bellwood-acad.org/bwa-starfall-soiree/</p>
  <p class="nonprofit-note">Bellwood is a 501(c)(3) organization</p>

  <div class="school-mark"><span class="mark-square"></span><span>Bellwood Catholic School</span></div>
  <address class="return-address">
    Bellwood Catholic School<br>482 North Quillan<br>Calder Falls, TX 75418
  </address>
  <div class="stamp-box"></div>
</section>

</body>
</html>
```